Business Card Design

I would like a logo created for the top left corner of the card please. I would like a checkerboard in a dark navy with the edges fading out and one random bright orange square.
Updates

I have attached some further notes and a really rough sketch of what I am after.  Thank you. :)

Target Market(s)

Construction, mining, mechanical

Industry/Entity Type

Business

Contact Information for Business Card

Korvane Works Pty Ltd, Glen Hadwick, P. 0418365072, F. 0736209158, E.glen@korvaneworks.com.au, PO Box 87 YARRAWONGA Q 4581, ABN 53209874611

Font styles to use
Sans Serif

Requirements
Must have
• Really Dark Navy
Really bright Orange

```html
<!DOCTYPE html>
<html lang="en">
<head>
<meta charset="utf-8">
<title>Korvane Works – Business Card</title>
<link rel="stylesheet" href="https://fonts.googleapis.com/css2?family=Jost:wght@400;600&display=swap">
<style>
  :root {
    --navy: #000080;
    --orange: #ff8000;
    --white: #ffffff;
    --mark-tone: #8c8cc4;
  }
  html, body {
    margin: 0;
    padding: 0;
    width: 1200px;
    height: 727px;
    overflow: hidden;
    background: var(--white);
  }
  .card {
    position: relative;
    width: 1200px;
    height: 727px;
    background: var(--white);
    font-family: "Jost", "Century Gothic", sans-serif;
    color: var(--navy);
    overflow: hidden;
  }
  .mark-area {
    position: absolute;
    left: 0;
    top: 0;
    width: 416px;
    height: 416px;
    background: var(--mark-tone);
  }
  .brand-name {
    position: absolute;
    right: 60px;
    top: 150px;
    margin: 0;
    font-size: 68px;
    font-weight: 600;
    line-height: 1;
    white-space: nowrap;
  }
  .company {
    position: absolute;
    right: 60px;
    top: 262px;
    margin: 0;
    font-size: 31px;
    font-weight: 400;
    line-height: 1;
    white-space: nowrap;
  }
  .person-name {
    position: absolute;
    right: 60px;
    top: 376px;
    margin: 0;
    font-size: 48px;
    font-weight: 600;
    line-height: 1;
    white-space: nowrap;
  }
  .mobile {
    position: absolute;
    right: 60px;
    top: 436px;
    margin: 0;
    font-size: 33px;
    font-weight: 400;
    line-height: 1;
    white-space: nowrap;
  }
  .contact-band {
    position: absolute;
    left: 0;
    top: 549px;
    width: 1200px;
    height: 178px;
    background: var(--orange);
    color: var(--white);
    font-size: 31px;
    line-height: 1;
  }
  .contact-band p {
    position: absolute;
    margin: 0;
    white-space: nowrap;
  }
  .postal { left: 64px; top: 56px; }
  .abn { left: 66px; top: 108px; }
  .fax { right: 60px; top: 56px; }
  .email { right: 60px; top: 108px; }
</style>
</head>
<body>
  <main class="card">
    <div class="mark-area" role="img" aria-label="Company logo mark area"></div>
    <p class="brand-name">Korvane Works</p>
    <p class="company">Korvane Works Pty Ltd</p>
    <p class="person-name">Glen Hadwick</p>
    <p class="mobile">0418 365 072</p>
    <section class="contact-band">
      <p class="postal">PO Box 87 YARRAWONGA Q 4581</p>
      <p class="abn">ABN 53 209 874 611</p>
      <p class="fax">F. 0736 209 158</p>
      <p class="email">E.glen@korvaneworks.com.au</p>
    </section>
  </main>
</body>
</html>
```